依頼概要
■ 依頼の目的/概要

弊社は学習塾を運営しております。
店舗前に目を引くのぼりをデザインしていただければと思います。

■ 重視する点/検討基準

たまたま通りかかったお母さんが「ちょっと話だけでも聞いてみようかしら」と思うような「入りやすい」「相談してみたい」「親しみがある」デザインが希望です。

塾ですが、あまり固いイメージではなく、いきすぎない程度にポップな感じも可です。

また、のぼりには以下の言葉を入れてください。

「忘れる前に解かせます。」
「緊張感指導と細分化個別指導」
「圧倒!5倍の演習量!」

出来れば色違いで上記の言葉がそれぞれ入った3種類を作っていただけると非常にありがたいです。
また、それぞれの中に

「学習相談・進路相談 受付中」
「おきがるにどうぞ」

などの言葉を入れてください。

一応、ロゴも添付しましたが、
これは使わなくても良いと思います。

参考までに店舗前の1例として添付の写真をご覧になってください。

■ のぼりの情報

サイズ:横450×縦1800

■ 納品ファイルの希望

イラストレーターver.10形式でお願いします。

■ 利用用途

店舗前のぼり

■ その他/注意点

選択させて頂いたデザインの著作権(財産権)等の扱いはQuimbel利用規約に従い、弊社に譲渡をお願いします。フォントや画像素材などを利用する場合は上記利用用途に使用できることを確認し、第三者の知的財産権等に注意して下さい。
■ 選んだ理由

矢印のデザインがインパクトがあり、POPになりすぎずに学習塾らしかったところです。
オリジナルでキャッチも考えていただいたのもバッチリでした。

■ 提案者全員のお礼・コメント

ご提案いただいたみなさん、ありがとうございました。

```html
<!DOCTYPE html>
<html lang="ja">
<head>
<meta charset="utf-8">
<title>学習塾のぼり 3種</title>
<link href="https://fonts.googleapis.com/css2?family=Noto+Sans+JP:wght@700;900&display=swap" rel="stylesheet">
<style>
  :root {
    --green: #8cb23e;
    --orange: #e8621c;
    --ink: #1a1a1a;
    --white: #ffffff;
    --backdrop: #eeeeee;
  }
  * { margin: 0; padding: 0; box-sizing: border-box; }
  html, body { width: 851px; height: 1200px; overflow: hidden; }
  body {
    background: var(--backdrop);
    font-family: "Noto Sans JP", sans-serif;
    position: relative;
  }
  .banner {
    position: absolute;
    top: 119px;
    width: 238px;
    height: 1017px;
    background: var(--white);
    display: flex;
    flex-direction: column;
  }
  .banner--forget { left: 34px; }
  .banner--practice { left: 308px; }
  .banner--focus { left: 584px; }

  .brand-band {
    height: 70px;
    background: var(--green);
    display: flex;
    align-items: center;
    justify-content: center;
    gap: 8px;
  }
  .brand-mark { width: 14px; height: 14px; background: var(--white); }
  .brand-name {
    color: var(--white);
    font-weight: 900;
    font-size: 28px;
    letter-spacing: 1px;
  }

  .message {
    flex: 1;
    padding: 14px 10px 0;
    display: flex;
    flex-direction: column;
    align-items: center;
  }
  .lead-char {
    color: var(--orange);
    font-weight: 900;
    font-size: 170px;
    line-height: 1;
    margin-top: 6px;
  }
  .columns {
    display: flex;
    flex-direction: row-reverse;
    justify-content: center;
    gap: 4px;
    margin-top: 6px;
  }
  .col {
    writing-mode: vertical-rl;
    font-weight: 900;
    line-height: 1;
    letter-spacing: 0;
  }
  .col--accent { color: var(--orange); }
  .col--body { color: var(--ink); }

  .banner--forget .col--accent { font-size: 100px; }
  .banner--forget .col--body { font-size: 68px; margin-top: 60px; }
  .banner--practice .col--accent { font-size: 100px; }
  .banner--practice .col--body { font-size: 60px; margin-top: 12px; }
  .banner--focus .col--accent { font-size: 82px; }
  .banner--focus .col--body { font-size: 56px; margin-top: 6px; }

  .consult {
    margin: 0 14px 28px;
    height: 232px;
    background: var(--green);
    display: flex;
    flex-direction: column;
    justify-content: center;
    padding: 10px 14px;
  }
  .consult-line {
    flex: 1;
    display: flex;
    align-items: center;
    justify-content: center;
    color: var(--white);
    font-weight: 900;
    font-size: 40px;
    letter-spacing: 4px;
    border-bottom: 3px solid var(--white);
  }
  .consult-line:last-child { border-bottom: none; }
</style>
</head>
<body>

  <section class="banner banner--forget">
    <header class="brand-band"><span class="brand-mark"></span><span class="brand-name">STEPLINE</span></header>
    <div class="message">
      <div class="lead-char">忘</div>
      <div class="columns">
        <p class="col col--accent">れる前に</p>
        <p class="col col--body">解かせます。</p>
      </div>
    </div>
    <div class="consult">
      <div class="consult-line">進路相談</div>
      <div class="consult-line">学習相談</div>
      <div class="consult-line">受付中</div>
    </div>
  </section>

  <section class="banner banner--practice">
    <header class="brand-band"><span class="brand-mark"></span><span class="brand-name">STEPLINE</span></header>
    <div class="message">
      <div class="lead-char">圧</div>
      <div class="columns">
        <p class="col col--accent">倒！</p>
        <p class="col col--body">5倍の演習量!!</p>
      </div>
    </div>
    <div class="consult">
      <div class="consult-line">進路相談</div>
      <div class="consult-line">学習相談</div>
      <div class="consult-line">受付中</div>
    </div>
  </section>

  <section class="banner banner--focus">
    <header class="brand-band"><span class="brand-mark"></span><span class="brand-name">STEPLINE</span></header>
    <div class="message">
      <div class="lead-char">緊</div>
      <div class="columns">
        <p class="col col--accent">張感指導と</p>
        <p class="col col--body">細分化個別指導</p>
      </div>
    </div>
    <div class="consult">
      <div class="consult-line">進路相談</div>
      <div class="consult-line">学習相談</div>
      <div class="consult-line">受付中</div>
    </div>
  </section>

</body>
</html>
```